Poster for a new "Pizza Roll" Combo at our bakery

We are a cinnamon roll and coffee focused bakery, but we would like an innovative poster design to bring attention to our new offering, a Pizza Roll. We will be offering it as a combo, and this is what we wish to advertise. It will be geared mainly towards a younger high school aged crowd. I have included pics of the Pizza Rolls, but it's up to you how you want to incorporate them in the design.Poster should include our logo, the pizza rolls, and can include a drink to illustrate the combo as well. ( we offer710 ml vima bottle products and lurn bottled waters)Main Text: Try our amazing new Pizza Rolls! Message to get accross: $6.00 for a Pizza Roll and drink.Small Print: Avail after 11am, while supplies last. Includes one pizza roll and one bottled drink of choice. Taxes extra.

Target Market(s)

Broad, but mainly high school aged kids

Industry/Entity Type

Bakery

Colors

Designer to choose colors to be used in the design.

Requirements
Must have
• Text: " Try our amazing new PIzza Rolls!:
• $6 Pizza Roll Combo (Pizza Roll and a drink)
Nice to have
• Pic of the PIzza Roll (photo shopped if needed to improve esthetics)
• Pic of a Bottled 710ml vima drink
Should not have
• Any animal product references, as we are a Vegan shop.

```html
<!DOCTYPE html>
<html lang="en">
<head>
<meta charset="utf-8">
<title>Pizza Roll Combo Poster</title>
<link href="https://fonts.googleapis.com/css2?family=Kaushan+Script&family=Alfa+Slab+One&family=Oswald:wght@600;700&family=Roboto:wght@400&display=swap" rel="stylesheet">
<style>
  :root {
    --sun-core: #ffd23a;
    --sun-mid: #ff9a1a;
    --sun-edge: #e8560c;
    --banner-blue: #253c9a;
    --banner-blue-dark: #17286e;
    --roll-red: #d7262b;
    --combo-red: #b91c22;
    --price-yellow: #ffd21f;
    --white: #ffffff;
    --dough: #e6bb85;
    --dough-dark: #b9763c;
    --cola: #6a2214;
    --cola-dark: #2e0c06;
  }
  html, body { margin: 0; padding: 0; overflow: hidden; }
  body { width: 849px; height: 1200px; background: #fff; }
  .poster {
    position: relative;
    width: 849px; height: 1200px; overflow: hidden;
    background: radial-gradient(circle at 45% 45%, var(--sun-core) 0%, var(--sun-mid) 40%, var(--sun-edge) 100%);
  }
  .headline-script {
    position: absolute; margin: 0;
    font-family: "Kaushan Script", cursive;
    color: var(--white); font-weight: 400;
    text-shadow: 0 4px 6px rgba(120,40,0,.35);
    transform: rotate(-4deg);
    line-height: 1; white-space: nowrap;
  }
  .headline-script--first { left: 85px; top: 22px; font-size: 104px; }
  .headline-script--second { left: 235px; top: 128px; font-size: 96px; }

  .rolls-photo {
    position: absolute; left: 400px; top: 345px; width: 449px; height: 500px;
    background: radial-gradient(circle at 45% 55%, var(--dough) 0%, var(--dough-dark) 90%);
    border-radius: 8px 0 0 8px;
    box-shadow: -4px 6px 14px rgba(90,30,0,.35);
  }
  .drink-photo {
    position: absolute; left: 170px; top: 565px; width: 130px; height: 340px;
    background: linear-gradient(90deg, var(--cola-dark) 0%, var(--cola) 45%, var(--cola-dark) 100%);
    border-radius: 14px;
  }

  .title-block { position: absolute; left: 0; top: 0; width: 849px; height: 560px; }
  .banner-pizza {
    position: absolute; left: 55px; top: 290px; width: 600px; height: 150px;
    background: var(--banner-blue);
    border: 5px solid var(--white);
    box-shadow: 6px 8px 0 var(--banner-blue-dark);
    transform: rotate(-5deg);
    display: flex; align-items: center; justify-content: center;
  }
  .banner-pizza span {
    font-family: "Alfa Slab One", serif; font-size: 140px; color: var(--white);
    letter-spacing: 4px; line-height: 1; padding-top: 20px;
  }
  .tag-new {
    position: absolute; left: 65px; top: 262px;
    font-family: "Alfa Slab One", serif; font-size: 68px; color: var(--price-yellow);
    transform: rotate(-8deg);
    -webkit-text-stroke: 3px var(--roll-red);
    line-height: 1;
  }
  .banner-rolls {
    position: absolute; left: 215px; top: 430px; width: 410px; height: 115px;
    background: var(--roll-red);
    border: 5px solid var(--white);
    transform: rotate(-5deg);
    display: flex; align-items: center; justify-content: center;
    box-shadow: 5px 7px 0 rgba(100,10,10,.4);
  }
  .banner-rolls span {
    font-family: "Alfa Slab One", serif; font-size: 96px; color: var(--white); line-height: 1;
  }

  .combo-band {
    position: absolute; left: -20px; top: 915px; width: 590px; height: 140px;
    background: var(--white);
    transform: rotate(-2deg);
    box-shadow: 0 6px 10px rgba(100,30,0,.3);
  }
  .combo-label {
    position: absolute; left: 55px; top: 922px; margin: 0;
    font-family: "Oswald", sans-serif; font-weight: 700; line-height: .95;
    transform: rotate(-2deg);
    text-transform: uppercase;
  }
  .combo-label .line-a { display: block; font-size: 68px; color: var(--roll-red); }
  .combo-label .line-b { display: block; font-size: 68px; color: var(--combo-red); }

  .price {
    position: absolute; left: 505px; top: 790px;
    font-family: "Alfa Slab One", serif; color: var(--price-yellow);
    -webkit-text-stroke: 4px var(--banner-blue);
    text-shadow: 6px 8px 0 rgba(120,40,0,.35);
    line-height: 1; white-space: nowrap;
  }
  .price .currency { font-size: 150px; vertical-align: 40px; }
  .price .amount { font-size: 300px; }

  .fine-print {
    position: absolute; left: 0; top: 1092px; width: 849px; margin: 0;
    text-align: center; font-family: "Roboto", sans-serif; font-size: 25px;
    color: var(--white); line-height: 1.35;
  }
</style>
</head>
<body>
  <main class="poster">
    <h1 class="headline-script headline-script--first">Try out</h1>
    <p class="headline-script headline-script--second">our amazing</p>

    <div class="rolls-photo" role="img" aria-label="Photo of freshly baked pizza rolls with tomato swirls"></div>
    <div class="drink-photo" role="img" aria-label="Photo of a 710 ml bottle of vima soft drink"></div>

    <div class="title-block">
      <div class="banner-pizza"><span>PIZZA</span></div>
      <div class="tag-new">NEW</div>
      <div class="banner-rolls"><span>Rolls!</span></div>
    </div>

    <div class="combo-band"></div>
    <h2 class="combo-label">
      <span class="line-a">Pizza Roll</span>
      <span class="line-b">Combo</span>
    </h2>
    <div class="price"><span class="currency">$</span><span class="amount">6</span></div>

    <p class="fine-print">Available after 11am, while supplies last.<br>Includes one pizza roll and one bottled drink of choice. Taxes extra.</p>
  </main>
</body>
</html>
```